Business Card and Logo Color Scheme Design Contest

We are starting a new company called Lone Ridge Structural Partners and already have a logo however, the colors for the logo itself are not final and COULD be changed. I'm hoping to move AWAYfrom the gold color in the card and the logo as it seems a bit outdated. What we need help with is to find what our business color scheme will be, and then incorporate those colors into both the logo and the business card design itself. We also want to make sure we are known as "LRS" so in the future we can just refer to ourselves as "LRS" and not Lone Ridge Structural Partners. That being said, I would like to make a slight change to the logo to somehow include the letters "LRS." The logo used in the front of the card design MUST ALSO include the words "Firm No. 64307" within the logo. My vision is for the front of the card to have the information shown in the attached image. For the back of the card, I'm hoping to have something very simple. I'm envisioning a solid color with either the website (www.bridgemarkplans.com) and a simplified version of the logo. I've attached an example but I'm looking for a complete redesign. I'm looking for a slick, modern and simple design.

Industry/Entity Type

Civil Engineer

Contact Information for Business Card

Logo
Firm No. 64307
Marcus Holloway, PE
Chief Operating Officer
Email:mholloway@bridgemarkplans.com
Ph: 936.555.0142 | D: 936.555.0178 | M:210.555.0263
4187 W. Kellingham, Conroe, Texas 77301
www.bridgemarkplans.com

Requirements
Must have
• Logo
Contact Info
Nice to have
• "LRS" Incorporated in the design
Should not have
• The current color scheme

```html
<!DOCTYPE html>
<html lang="en">
<head>
<meta charset="utf-8">
<title>LRS Business Card</title>
<link href="https://fonts.googleapis.com/css2?family=Libre+Caslon+Text:wght@400;700&family=Open+Sans:wght@400;600&display=swap" rel="stylesheet">
<style>
  :root {
    --maroon: #8a0538;
    --maroon-deep: #74032f;
    --maroon-tint: #9c1a4a;
    --grey: #6e6e70;
    --ink: #3d3d3f;
    --paper: #ffffff;
    --backdrop: #e8ebeb;
  }
  * { margin: 0; padding: 0; box-sizing: border-box; }
  html, body { width: 1200px; height: 900px; overflow: hidden; }
  body {
    background: var(--backdrop);
    position: relative;
    font-family: "Libre Caslon Text", Georgia, serif;
  }
  .card {
    position: absolute;
    width: 640px;
    height: 366px;
    box-shadow: 0 6px 18px rgba(0,0,0,0.12);
    overflow: hidden;
  }
  /* Back of card */
  .card-back {
    left: 80px; top: 60px;
    background: var(--maroon);
    color: var(--paper);
  }
  .card-back .faint-mark {
    position: absolute;
    left: 200px; top: 70px;
    width: 200px; height: 200px;
    background: var(--maroon-deep);
    opacity: 0.7;
  }
  .card-back .brand {
    position: absolute;
    left: 150px; top: 118px;
    display: flex; align-items: center; gap: 18px;
  }
  .brand-square {
    width: 58px; height: 58px;
    background: currentColor;
    flex: none;
  }
  .brand-text { border-left: 1.5px solid currentColor; padding-left: 14px; }
  .brand-name {
    font-weight: 700;
    font-size: 24px;
    line-height: 1.02;
    text-transform: uppercase;
    letter-spacing: 0.5px;
  }
  .brand-rule { height: 1.5px; background: currentColor; margin: 6px 0 4px; width: 100%; }
  .firm-no { font-size: 10px; font-weight: 700; letter-spacing: 0.3px; }
  .card-back .website {
    position: absolute;
    left: 0; right: 0; bottom: 58px;
    text-align: center;
    font-family: "Open Sans", Arial, sans-serif;
    font-size: 15px;
    letter-spacing: 4px;
  }
  /* Front of card */
  .card-front {
    left: 480px; top: 474px;
    background: var(--paper);
  }
  .card-front .brand {
    position: absolute;
    left: 44px; top: 62px;
    display: flex; align-items: center; gap: 16px;
    color: var(--maroon);
  }
  .card-front .brand-name { font-size: 21px; }
  .card-front .firm-no { color: var(--maroon); }
  .person {
    position: absolute;
    left: 44px; top: 232px;
  }
  .person-name {
    color: var(--maroon);
    font-weight: 700;
    font-size: 24px;
  }
  .person-title {
    color: var(--grey);
    font-weight: 700;
    font-size: 14px;
    margin-top: 4px;
  }
  .divider {
    position: absolute;
    left: 372px; top: 70px;
    width: 1.5px; height: 220px;
    background: var(--maroon);
  }
  .contact {
    position: absolute;
    left: 394px; top: 108px;
    list-style: none;
    font-family: "Open Sans", Arial, sans-serif;
    font-size: 11.5px;
    color: var(--ink);
  }
  .contact li {
    display: flex; align-items: center; gap: 10px;
    height: 34px;
  }
  .contact svg { width: 20px; height: 20px; flex: none; }
</style>
</head>
<body>

<section class="card card-back" aria-label="Card back">
  <div class="faint-mark"></div>
  <div class="brand">
    <div class="brand-square"></div>
    <div class="brand-text">
      <div class="brand-name">Lone Ridge<br>Structural<br>Partners</div>
      <div class="brand-rule"></div>
      <div class="firm-no">Firm No. 64307</div>
    </div>
  </div>
  <div class="website">www.bridgemarkplans.com</div>
</section>

<section class="card card-front" aria-label="Card front">
  <div class="brand">
    <div class="brand-square"></div>
    <div class="brand-text">
      <div class="brand-name">Lone Ridge<br>Structural<br>Partners</div>
      <div class="brand-rule"></div>
      <div class="firm-no">Firm No. 64307</div>
    </div>
  </div>

  <div class="person">
    <div class="person-name">Marcus Holloway, PE</div>
    <div class="person-title">Chief Operating Officer</div>
  </div>

  <div class="divider"></div>

  <ul class="contact">
    <li>
      <svg viewBox="0 0 20 20"><circle cx="10" cy="10" r="10" fill="#8a0538"/><rect x="5.5" y="7" width="9" height="6" rx="1.5" fill="none" stroke="#fff" stroke-width="1.4"/><circle cx="10" cy="10" r="1.4" fill="#fff"/></svg>
      <span>936.555.0142 / 936.555.0178</span>
    </li>
    <li>
      <svg viewBox="0 0 20 20"><circle cx="10" cy="10" r="10" fill="#8a0538"/><rect x="7" y="4.5" width="6" height="11" rx="1.2" fill="none" stroke="#fff" stroke-width="1.4"/><circle cx="10" cy="13" r="0.8" fill="#fff"/></svg>
      <span>210.555.0263</span>
    </li>
    <li>
      <svg viewBox="0 0 20 20"><circle cx="10" cy="10" r="10" fill="#8a0538"/><rect x="5" y="6.5" width="10" height="7" fill="none" stroke="#fff" stroke-width="1.3"/><path d="M5 6.5 L10 10.5 L15 6.5" fill="none" stroke="#fff" stroke-width="1.3"/></svg>
      <span>mholloway@bridgemarkplans.com</span>
    </li>
    <li>
      <svg viewBox="0 0 20 20"><circle cx="10" cy="10" r="10" fill="#8a0538"/><path d="M10 15.5 C7 12 6.5 10.5 6.5 8.8 A3.5 3.5 0 0 1 13.5 8.8 C13.5 10.5 13 12 10 15.5 Z" fill="#fff"/><circle cx="10" cy="8.8" r="1.3" fill="#8a0538"/></svg>
      <span>4187 W. Kellingham, Conroe, Texas 77301</span>
    </li>
  </ul>
</section>

</body>
</html>
```